Create Template Proposal Coversheet

We need a proposal Cover Sheet & Page Template for residential architectural projects. For the Cover Sheet, we want a variety of images blends and set as a background image for the title of the proposal for prospective clients. We need it in a format that we can type over the top of the image (maybe whited-out in the middle) so we can use it for all our proposals. Our logo should be clear and sharp in a corner (but we will leave that up to the designer. Not all images need to be used. For the Page Template we want a consistent look on the page with our logo, company address & contact information and a design element that ties the entire proposal together. Our proposals consist of a Cover page, Project information sheet, a picture of the property, the proposal for services (3-5 pages), Expect fees page and a timeline page.

Target Market(s)

Homeowners, 35 - 60 years old

Industry/Entity Type

Architecture

Font styles to use
Serif

Colors
3176b5
f68d4c
ec1f27
fbee3f

Requirements
Must have
• The cover should have a nice blend of images - looking for something that shows the whole design process - from initial sketches to working drawings, construction and finished home. These images are background to the title of the proposal

```html
<!DOCTYPE html>
<html lang="en">
<head>
<meta charset="UTF-8">
<title>Proposal Cover</title>
<link rel="stylesheet" href="https://fonts.googleapis.com/css2?family=Montserrat:wght@500;600;700&display=swap">
<style>
  :root {
    --frame: #000000;
    --blue-deep: #0f55d8;
    --blue-bright: #1790f0;
    --orange: #fb8310;
    --white: #ffffff;
    --photo-sky: #e6e8ec;
    --photo-glass: #6f8a8c;
  }
  html, body { margin: 0; padding: 0; overflow: hidden; }
  body { width: 853px; height: 1200px; background: var(--frame); }
  .cover {
    position: relative;
    width: 853px;
    height: 1200px;
    overflow: hidden;
    font-family: "Montserrat", Arial, sans-serif;
    color: var(--white);
  }
  .cover-art { position: absolute; inset: 0; display: block; }
  .brand {
    position: absolute;
    left: 588px;
    top: 650px;
    width: 200px;
    text-align: center;
    font-weight: 600;
    font-size: 19px;
    letter-spacing: 0.5px;
    line-height: 1;
    color: var(--white);
  }
  .title-block { position: absolute; left: 94px; top: 916px; }
  .proposal-title {
    margin: 0;
    font-weight: 700;
    font-size: 45px;
    line-height: 1;
    letter-spacing: 0.2px;
  }
  .title-rule {
    width: 400px;
    height: 1.5px;
    margin: 19px 0 0 4px;
    background: var(--orange);
  }
  .tagline {
    margin: 19px 0 0 3px;
    font-weight: 500;
    font-size: 27px;
    line-height: 35px;
  }
</style>
</head>
<body>
<main class="cover">
  <svg class="cover-art" width="853" height="1200" viewBox="0 0 853 1200" xmlns="http://www.w3.org/2000/svg">
    <defs>
      <linearGradient id="photoTone" x1="0" y1="0" x2="0.3" y2="1">
        <stop offset="0" stop-color="var(--photo-sky)"/>
        <stop offset="0.35" stop-color="#c9ced6"/>
        <stop offset="1" stop-color="var(--photo-glass)"/>
      </linearGradient>
      <linearGradient id="blueField" x1="0" y1="0" x2="1" y2="1">
        <stop offset="0" stop-color="var(--blue-deep)"/>
        <stop offset="1" stop-color="var(--blue-bright)"/>
      </linearGradient>
    </defs>
    <rect x="0" y="0" width="853" height="1200" fill="var(--frame)"/>
    <rect class="building-photo" x="22" y="29" width="810" height="700" fill="url(#photoTone)"
          role="img" aria-label="Photograph of a modern glass and aluminium office building under a cloudy sky"/>
    <polygon class="orange-wedge" points="440,652 832,408 832,716 688,792" fill="var(--orange)"/>
    <polygon class="blue-field" points="22,412 440,652 688,792 832,716 832,1180 22,1180" fill="url(#blueField)"
             role="img" aria-label="Rolled architectural blueprints tinted blue"/>
  </svg>

  <div class="brand">Harlan Reed Architect</div>

  <section class="title-block">
    <h1 class="proposal-title">Title For Proposal</h1>
    <div class="title-rule"></div>
    <p class="tagline">30 Years of Creative<br>Precision &amp; Professional Designs</p>
  </section>
</main>
</body>
</html>
```